Business card design for Velvet Harbor

We need business cards designed for our new marketing consulting company, Velvet Harbor. Our services include marketing strategy, go-to-market and launch planning, growth strategy, and execution. We serve medical technology and health technology companies, from startups to well-established growth companies.

The business cards should feel professional, credible, reliable and trustworthy, and should instill confidence. Also bold, creative, and modern.

The design must use the Velvet Harbor logo.

The primary brand color is this orange: #FF5501
A secondary color that you can use is this gray: #282B2D
I would prefer only to use the orange and gray. But if you feel you really need an additional accent color (please use it very sparingly, as little as possible), you can use this blue for small accent purposes: #009FED

Attached are the logo files. The main logo is the one with a little bit of orange on the left and the rest is gray.

The business card should include the following:

Velvet Harbor logo
First name and last name
Title
Email address
Phone number and type (in whatever order looks best for the design
Website (the website does not need to be in the same block as the personal info)

For example:

Nessa Pryle
Founder & Principal
nessa@velvetharbor.com
+1.628.309.4156 mobile (can use "." or spaces in between blocks of numbers)
velvetharbor.com (somewhere on the card, it does not need to be with the personal info; and note that there is no "www." at the beginning)

Note that there will be no address listed on the business card.

Target Market(s)

Executives (CEO, head of marketing, head of sales) at medical technology and health technology companies, mostly in their 40s and older, well-educated, often with advanced degrees. They are strategic thinkers, responsible for budgets, and familiar with P&L. Their comfort with and trust in using outside consultants varies.

Industry/Entity Type

Medical technology and health technology companies.

Contact Information for Business Card

See project description

Font styles to use
Sans Serif

Requirements
Must have
• Logo and see Business card details section above.

```html
<!DOCTYPE html>
<html lang="en">
<head>
<meta charset="utf-8">
<title>Velvet Harbor — Business Card</title>
<link rel="stylesheet" href="https://fonts.googleapis.com/css2?family=Roboto:wght@400;500;700&display=swap">
<style>
  :root {
    --brand-orange: #F05A22;
    --brand-gray: #2B2C2E;
    --card-white: #F3F3F3;
    --band-gray: #D2D2D3;
    --backdrop: #1C1C1D;
    --text-white: #FFFFFF;
  }
  * { box-sizing: border-box; margin: 0; padding: 0; }
  html, body {
    width: 1200px; height: 899px; overflow: hidden;
    background: var(--backdrop);
    font-family: "Roboto", Arial, sans-serif;
  }
  .stage { position: relative; width: 1200px; height: 899px; }
  .card {
    position: absolute; left: 332px; width: 556px; height: 317px;
    overflow: hidden; box-shadow: 0 4px 14px rgba(0,0,0,.55);
  }
  .card--front { top: 132px; background: var(--card-white); }
  .card--back { top: 486px; background: var(--brand-orange); }

  .wave { position: absolute; inset: 0; width: 100%; height: 100%; }

  .identity { position: absolute; left: 25px; top: 30px; }
  .identity__name {
    font-size: 20px; font-weight: 500; color: var(--brand-gray);
    text-transform: uppercase; letter-spacing: .2px; line-height: 1;
  }
  .identity__first { color: var(--brand-orange); }
  .identity__title {
    margin-top: 6px; font-size: 12px; color: var(--brand-orange);
  }

  .wordmark {
    position: absolute; text-transform: uppercase; font-weight: 500;
    line-height: 1;
  }
  .wordmark--front {
    right: 36px; top: 40px; font-size: 14px; letter-spacing: 2px;
    color: var(--brand-gray);
  }
  .wordmark--back {
    left: 0; right: 0; top: 132px; text-align: center;
    font-size: 27px; letter-spacing: 5px; color: var(--card-white);
  }
  .wordmark span { display: block; }
  .wordmark--back span + span { margin-top: 6px; }

  .contact {
    position: absolute; left: 26px; top: 249px; list-style: none;
    color: var(--text-white); font-size: 12px;
  }
  .contact__item { display: flex; align-items: center; height: 16px; }
  .contact__icon { width: 9px; height: 9px; margin-right: 10px; fill: var(--text-white); }
</style>
</head>
<body>
<main class="stage">
  <section class="card card--front" aria-label="Business card front">
    <svg class="wave" viewBox="0 0 526 300" preserveAspectRatio="none" aria-hidden="true">
      <path d="M0,150 C60,112 150,116 250,158 C340,198 420,214 526,190 L526,300 L0,300Z" fill="var(--band-gray)"/>
      <path d="M0,156 C80,126 170,134 260,174 C350,214 440,236 526,214 L526,300 L0,300Z" fill="var(--brand-gray)"/>
      <path d="M0,152 C70,132 160,140 240,180 C330,230 440,264 526,254 L526,300 L0,300Z" fill="var(--brand-orange)"/>
    </svg>

    <div class="identity">
      <h1 class="identity__name"><span class="identity__first">Nessa</span> Pryle</h1>
      <p class="identity__title">Founder &amp; Principal</p>
    </div>

    <div class="wordmark wordmark--front"><span>Velvet</span><span>Harbor</span></div>

    <ul class="contact">
      <li class="contact__item">
        <svg class="contact__icon" viewBox="0 0 10 10" aria-hidden="true"><path d="M2,0.5 L3.6,2.6 L2.8,3.6 C3.4,5 4.9,6.6 6.4,7.2 L7.4,6.4 L9.5,8 L8.6,9.5 C4.6,9.4 0.6,5.4 0.5,1.4Z"/></svg>
        <span>+1 628 309 4156</span>
      </li>
      <li class="contact__item">
        <svg class="contact__icon" viewBox="0 0 10 10" aria-hidden="true"><path d="M0,2 H10 V8.5 H0Z M0.8,2.6 L5,5.6 L9.2,2.6" stroke="var(--brand-orange)" stroke-width=".8"/></svg>
        <span>nessa@velvetharbor.com</span>
      </li>
      <li class="contact__item">
        <svg class="contact__icon" viewBox="0 0 10 10" aria-hidden="true"><circle cx="5" cy="5" r="4.6"/><path d="M3,2.5 L5,3.5 L4,5.5 L2,4.5Z M6,6 L7.8,6.5 L6.5,8.3Z" fill="var(--brand-orange)"/></svg>
        <span>www.velvetharbor.com</span>
      </li>
    </ul>
  </section>

  <section class="card card--back" aria-label="Business card back">
    <div class="wordmark wordmark--back"><span>Velvet</span><span>Harbor</span></div>
  </section>
</main>
</body>
</html>
```